브랜드 소개
저희 브랜드 루미(LUMI)는,
스테이크(STAKE)와 쉬림프(SHRIMP), 가지고 가다(TAKE OUT)의 단어를 결합한 합성어로써, 레스토랑에서 즐길 수 있는 쉬림프와 스테이크를 간편하게 드실 수 있도록 지은 이름입니다.
현재 프랜차이즈 가맹사업을 하고 있으며, 신메뉴 출시로 인한 포스터 디자인을 공모합니다.

```html
<!DOCTYPE html>
<html lang="ko">
<head>
<meta charset="utf-8">
<title>LUMI 신메뉴 포스터</title>
<link href="https://fonts.googleapis.com/css2?family=Black+Han+Sans&family=Nanum+Pen+Script&family=Yellowtail&family=Noto+Sans+KR:wght@500;700&display=swap" rel="stylesheet">
<style>
  :root {
    --backdrop: #eeeeee;
    --red: #a81f1d;
    --bar: #33190d;
    --white: #ffffff;
    --yellow: #f6c11e;
    --badge: #f3a31c;
    --badge-text: #b3201c;
    --beige: #e9d4b6;
  }
  * { margin: 0; padding: 0; box-sizing: border-box; }
  html, body { width: 1200px; height: 1200px; overflow: hidden; background: var(--backdrop); }
  .poster {
    position: absolute; left: 220px; top: 60px; width: 760px; height: 1080px;
    overflow: hidden; background: var(--red);
    font-family: 'Noto Sans KR', sans-serif;
  }
  .poster__field { position: absolute; inset: 0; }
  .dish {
    position: absolute; border-radius: 50%;
    box-shadow: 0 18px 30px rgba(0,0,0,.45);
  }
  .dish--spicy {
    left: 20px; top: 330px; width: 480px; height: 290px;
    background: radial-gradient(ellipse at 55% 45%, #d9432a 0%, #c8552e 35%, #b89a5c 64%, #2a2522 76%, #1b1816 100%);
  }
  .dish--bbq {
    left: 250px; top: 540px; width: 460px; height: 300px;
    background: radial-gradient(ellipse at 55% 50%, #c9672f 0%, #cf8a45 35%, #bfa56a 64%, #2a2522 76%, #1b1816 100%);
  }
  .script {
    position: absolute; font-family: 'Yellowtail', cursive; color: var(--white);
    font-size: 42px; line-height: 1.1; white-space: nowrap;
  }
  .script--spicy { left: 70px; top: 150px; transform: rotate(-13deg); }
  .script--bbq { left: 470px; top: 820px; transform: rotate(-11deg); }
  .badge {
    position: absolute; background: var(--badge); color: var(--badge-text);
    font-weight: 700; font-style: italic;
    font-size: 28px; line-height: 38px; padding: 0 14px; height: 38px;
  }
  .badge--spicy { right: 60px; top: 92px; }
  .badge--bbq { left: 70px; top: 702px; }
  .menu-title {
    position: absolute; font-family: 'Black Han Sans', sans-serif; color: var(--white);
    font-size: 70px; line-height: 74px; letter-spacing: -1px; white-space: nowrap;
  }
  .menu-title--spicy { right: 56px; top: 136px; text-align: right; }
  .menu-title--bbq { left: 66px; top: 746px; text-align: left; }
  .tagline {
    position: absolute; font-family: 'Nanum Pen Script', cursive; color: var(--yellow);
    font-size: 24px; line-height: 26px; white-space: nowrap;
  }
  .tagline--spicy { right: 60px; top: 292px; text-align: right; }
  .tagline--bbq { left: 70px; top: 930px; }
  .price-bar {
    position: absolute; left: 0; bottom: 0; width: 100%; height: 84px;
    background: var(--bar); display: flex; align-items: center; padding: 0 44px 0 70px;
    color: var(--beige);
  }
  .price-bar__menu { font-size: 19px; font-weight: 500; }
  .price-bar__price { font-size: 27px; font-weight: 700; margin-left: 20px; }
  .brand { margin-left: auto; display: flex; align-items: center; gap: 8px; }
  .brand__mark { width: 10px; height: 10px; background: var(--beige); }
  .brand__name { font-family: 'Black Han Sans', sans-serif; font-size: 32px; color: var(--beige); letter-spacing: 1px; }
</style>
</head>
<body>
<main class="poster">
  <svg class="poster__field" width="760" height="1080" viewBox="0 0 760 1080" aria-hidden="true">
    <defs>
      <linearGradient id="redTone" x1="0" y1="0" x2="0" y2="1">
        <stop offset="0" stop-color="#b02320"/>
        <stop offset="1" stop-color="#8c1916"/>
      </linearGradient>
      <linearGradient id="brownTone" x1="0" y1="0" x2="0" y2="1">
        <stop offset="0" stop-color="#62321d"/>
        <stop offset="1" stop-color="#4a2515"/>
      </linearGradient>
    </defs>
    <rect x="0" y="0" width="760" height="1080" fill="url(#redTone)"/>
    <polygon points="0,700 760,420 760,1080 0,1080" fill="url(#brownTone)"/>
  </svg>

  <div class="dish dish--spicy" role="img" aria-label="핫스파이시 쉬림프덮밥 사진: 매콤한 소스의 새우와 채소, 숙주를 올린 덮밥 그릇"></div>
  <div class="dish dish--bbq" role="img" aria-label="바베큐 쉬림프덮밥 사진: 바베큐 소스 새우와 채소, 숙주를 올린 덮밥 그릇"></div>

  <p class="script script--spicy">Hot Spicy<br>&nbsp;&nbsp;Shrimp Rice</p>
  <span class="badge badge--spicy">New</span>
  <h2 class="menu-title menu-title--spicy">핫스파이시<br>쉬림프덮밥</h2>
  <p class="tagline tagline--spicy">통통한 새우와 스파이시 소스의<br>화끈한 조화!</p>

  <span class="badge badge--bbq">New</span>
  <h2 class="menu-title menu-title--bbq">바베큐<br>쉬림프덮밥</h2>
  <p class="tagline tagline--bbq">통통한 새우와 바베큐 소스의 화려한 조화!</p>
  <p class="script script--bbq">Barbecue<br>&nbsp;Shrimp Rice</p>

  <footer class="price-bar">
    <span class="price-bar__menu">핫스파이시 쉬림프덮밥 &amp; 바베큐 쉬림프덮밥</span>
    <span class="price-bar__price">₩ 8,900</span>
    <span class="brand"><span class="brand__mark"></span><span class="brand__name">LUMI</span></span>
  </footer>
</main>
</body>
</html>
```